Quillrun Couriers Web design

Take a look at our existing website(www.qlnrun.com) and design a new one, plus coding and recreate an existing logo.

```html
<!DOCTYPE html>
<html lang="en">
<head>
<meta charset="utf-8">
<title>Quillrun Couriers</title>
<link href="https://fonts.googleapis.com/css2?family=Montserrat:wght@400;500;600;700&family=Open+Sans:wght@400;600&display=swap" rel="stylesheet">
<style>
:root{
  --orange:#f07f1b;
  --orange-dark:#d9690a;
  --blue:#1c5ea8;
  --blue-deep:#123f78;
  --ink:#2b2b2b;
  --muted:#6b6b6b;
  --line:#d9d9d9;
  --soft:#f3f3f3;
  --footer:#1a1a1a;
  --white:#ffffff;
}
*{box-sizing:border-box;margin:0;padding:0}
html,body{width:1200px;height:4144px;overflow:hidden}
body{font-family:"Open Sans",Arial,sans-serif;color:var(--ink);background:var(--white);position:relative}
h1,h2,h3,h4,.nav a,.btn{font-family:"Montserrat",Arial,sans-serif}
section,header,footer{position:relative;width:1200px;overflow:hidden}

/* header */
.site-header{height:112px;background:var(--white)}
.brand{position:absolute;left:112px;top:30px;display:flex;align-items:center;gap:12px}
.brand-square{width:22px;height:22px;background:var(--orange)}
.brand-name{font-family:"Montserrat",Arial,sans-serif;font-weight:700;font-size:26px;color:var(--blue)}
.topbar{position:absolute;right:56px;top:18px;display:flex;align-items:center;gap:26px;font-size:14px;color:var(--muted)}
.topbar span{display:flex;align-items:center;gap:8px}
.login{background:var(--orange);color:var(--white);font-family:"Montserrat",sans-serif;font-weight:600;font-size:12px;padding:6px 14px;border-radius:2px}
.nav{position:absolute;right:14px;top:68px;display:flex;gap:22px}
.nav a{font-size:15px;font-weight:500;color:var(--ink);text-decoration:none}
.nav a.active{color:var(--orange)}

/* hero */
.hero{height:600px}
.hero-photo{position:absolute;inset:0;background:linear-gradient(120deg,#b9c3cc 0%,#d8d2c6 45%,#ede8df 100%)}
.hero-tint{position:absolute;inset:0}
.hero-text{position:absolute;left:112px;top:240px;color:var(--white)}
.hero-text h1{font-size:48px;font-weight:700;line-height:1.12}
.hero-text p{font-size:22px;line-height:1.35;margin-top:18px;width:430px}
.btn-outline{display:inline-block;margin-top:34px;border:2px solid var(--white);color:var(--white);font-size:15px;font-weight:600;padding:14px 22px}
.dots{position:absolute;right:132px;bottom:80px;display:flex;gap:10px}
.dots i{width:12px;height:12px;border-radius:50%;background:rgba(255,255,255,.55)}
.dots i:first-child{background:var(--white)}

/* shared */
.section-title{text-align:center;font-size:34px;font-weight:700;color:var(--ink)}
.title-rule{width:150px;height:3px;margin:16px auto 0;background:linear-gradient(90deg,var(--blue) 50%,var(--orange) 50%)}
.btn{display:inline-block;background:var(--orange);color:var(--white);font-weight:600;font-size:15px;padding:15px 26px;border-radius:2px}

/* welcome */
.welcome{height:440px;text-align:center;padding-top:56px}
.welcome p{width:820px;margin:42px auto 0;font-size:16px;line-height:1.75;color:var(--muted)}
.welcome .btn{margin-top:44px}

/* services */
.services{height:628px;background:var(--soft);padding-top:72px}
.service-grid{display:flex;gap:20px;margin:64px 0 0 112px}
.service-card{width:312px;height:428px;background:var(--white);box-shadow:0 2px 8px rgba(0,0,0,.08)}
.service-img{height:228px}
.service-card h3{font-size:22px;font-weight:600;margin:22px 20px 8px}
.service-card p{font-size:14px;line-height:1.6;color:var(--muted);margin:0 20px;height:68px}
.service-card .more{display:block;margin:16px 20px 0;color:var(--orange);font-family:"Montserrat",sans-serif;font-weight:600;font-size:14px}

/* offer */
.offer{height:580px;padding-top:104px}
.offer-grid{display:flex;gap:28px;margin:70px 0 0 112px}
.offer-item{width:224px}
.offer-item svg{display:block;margin-left:4px}
.offer-item h4{font-size:20px;font-weight:600;margin:20px 0 12px}
.offer-item p{font-size:14px;line-height:1.6;color:var(--muted)}
.arrow{position:absolute;top:400px}

/* why */
.why{height:640px}
.why-photo{position:absolute;left:0;top:0;width:720px;height:640px;background:linear-gradient(135deg,#3a3a3a 0%,#6d6358 45%,#b8a58a 100%)}
.why-panel{position:absolute;inset:0}
.why-content{position:absolute;left:660px;top:66px;color:var(--white)}
.why-content h2{font-size:38px;font-weight:600}
.why-list{list-style:none;margin-top:40px}
.why-list li{display:flex;align-items:center;gap:14px;font-size:16px;height:36px}

/* contact */
.contact{height:688px;padding-top:70px}
.contact-form{width:880px;margin:74px auto 0;display:grid;grid-template-columns:1fr 1fr;column-gap:24px;row-gap:20px}
.field{height:44px;border:1px solid var(--line);padding:0 14px;display:flex;align-items:center;font-size:14px;color:#9a9a9a}
.field.wide{grid-column:1 / -1;height:104px;align-items:flex-start;padding-top:12px}
.contact .submit{display:block;width:112px;margin:36px auto 0;text-align:center;font-size:14px;padding:14px 0}

/* footer */
.site-footer{height:456px;background:var(--footer);color:#cfcfcf}
.footer-brand{position:absolute;left:112px;top:104px;display:flex;align-items:center;gap:12px}
.footer-brand .brand-name{color:var(--white)}
.footer-col{position:absolute;top:60px}
.footer-col h4{color:var(--white);font-size:18px;font-weight:600;margin-bottom:20px}
.footer-col li{list-style:none;font-size:15px;line-height:30px}
.contact-line{display:flex;gap:12px;font-size:14px;line-height:22px;margin-bottom:14px}
.contact-line svg{flex:none;margin-top:3px}
.footer-bottom{position:absolute;left:112px;right:112px;bottom:0;height:82px;border-top:1px solid #333;display:flex;align-items:center;justify-content:space-between;font-size:14px}
.social{display:flex;gap:14px}
.social i{width:34px;height:34px;border-radius:50%;border:1px solid #777}
</style>
</head>
<body>

<header class="site-header">
  <div class="brand"><span class="brand-square"></span><span class="brand-name">Quillrun Couriers</span></div>
  <div class="topbar">
    <span><svg width="14" height="14" viewBox="0 0 24 24"><path fill="#f07f1b" d="M6.6 10.8a15 15 0 0 0 6.6 6.6l2.2-2.2c.3-.3.7-.4 1-.2 1.1.4 2.3.6 3.6.6.6 0 1 .4 1 1V20c0 .6-.4 1-1 1A17 17 0 0 1 3 4c0-.6.4-1 1-1h3.5c.6 0 1 .4 1 1 0 1.3.2 2.5.6 3.6.1.3 0 .7-.2 1z"/></svg>555-014-7170</span>
    <span><svg width="16" height="12" viewBox="0 0 16 12"><rect x="1" y="1" width="14" height="10" fill="none" stroke="#f07f1b" stroke-width="1.6"/><path d="M1 1l7 6 7-6" fill="none" stroke="#f07f1b" stroke-width="1.6"/></svg>info@qlnrun.com</span>
    <span class="login">LOGIN</span>
  </div>
  <nav class="nav">
    <a class="active">Home</a><a>About Us</a><a>Services</a><a>Rates</a><a>Customer Benefits</a><a>Logistics</a><a>Contact Us</a>
  </nav>
</header>

<section class="hero">
  <div class="hero-photo" role="img" aria-label="Photo of two smiling colleagues reviewing a delivery on a tablet in a bright office"></div>
  <svg class="hero-tint" width="1200" height="600" viewBox="0 0 1200 600">
    <defs><linearGradient id="heroBlue" x1="0" x2="1"><stop offset="0" stop-color="#123f78" stop-opacity=".95"/><stop offset="1" stop-color="#1c5ea8" stop-opacity=".75"/></linearGradient></defs>
    <polygon points="0,0 560,0 700,600 0,600" fill="url(#heroBlue)"/>
  </svg>
  <div class="hero-text">
    <h1>Quillrun<br>Couriers</h1>
    <p>We are committed to providing professional messenger services.</p>
    <span class="btn btn-outline">GET MORE INFO</span>
  </div>
  <div class="dots"><i></i><i></i><i></i></div>
</section>

<section class="welcome">
  <h2 class="section-title">Welcome to Quillrun Couriers</h2>
  <div class="title-rule"></div>
  <p>We are committed to providing professional messenger services to care for the most important, emergency and time sensitive deliveries valuable to your company. Our services range from scheduled local and long distance, same day to all types of On-Demand services. Our goal is to become a leader by showing reliability, integrity as well as competitive pricing.</p>
  <span class="btn">READ MORE</span>
</section>

<section class="services">
  <h2 class="section-title">Our Services</h2>
  <div class="title-rule"></div>
  <div class="service-grid">
    <article class="service-card">
      <div class="service-img" role="img" aria-label="Photo of yellow medical record folders" style="background:linear-gradient(135deg,#e9c24a,#c9a567 60%,#8c6e4f)"></div>
      <h3>Hospital &amp; Medical Care</h3>
      <p>Hospital &amp; Medical Care – Home Deliveries, Pharmaceuticals and Critical Biotics.</p>
      <span class="more">READ MORE</span>
    </article>
    <article class="service-card">
      <div class="service-img" role="img" aria-label="Photo of stacked blue and white binders of banking documents" style="background:linear-gradient(135deg,#9fb6d6,#3f6fb3 55%,#dfe5ee)"></div>
      <h3>Banking &amp; Brokerage</h3>
      <p>Banking &amp; Brokerage – Emergency Deliveries, Mortgage Documents, Interoffice Routes.</p>
      <span class="more">READ MORE</span>
    </article>
    <article class="service-card">
      <div class="service-img" role="img" aria-label="Photo of labelled file folder tabs for taxes and insurance" style="background:linear-gradient(135deg,#e6e1d8,#b7ad9e 60%,#7d7466)"></div>
      <h3>Legal Filings</h3>
      <p>Legal, Administrative and sales deliveries associated with filing paperwork.</p>
      <span class="more">READ MORE</span>
    </article>
  </div>
</section>

<section class="offer">
  <h2 class="section-title">We Offer</h2>
  <div class="title-rule"></div>
  <svg class="arrow" style="left:40px" width="14" height="24" viewBox="0 0 14 24"><path d="M12 2L2 12l10 10" fill="none" stroke="#555" stroke-width="2.5"/></svg>
  <svg class="arrow" style="right:40px" width="14" height="24" viewBox="0 0 14 24"><path d="M2 2l10 10L2 22" fill="none" stroke="#555" stroke-width="2.5"/></svg>
  <div class="offer-grid">
    <div class="offer-item">
      <svg width="60" height="60" viewBox="0 0 60 60"><rect x="6" y="12" width="48" height="42" rx="4" fill="none" stroke="#1c5ea8" stroke-width="3"/><rect x="6" y="12" width="48" height="11" fill="#1c5ea8"/><rect x="16" y="5" width="4" height="12" fill="#f07f1b"/><rect x="40" y="5" width="4" height="12" fill="#f07f1b"/><g fill="#f07f1b"><rect x="14" y="30" width="7" height="6"/><rect x="26" y="30" width="7" height="6"/><rect x="38" y="30" width="7" height="6"/><rect x="14" y="41" width="7" height="6"/><rect x="26" y="41" width="7" height="6"/></g></svg>
      <h4>On-Demand</h4>
      <p>Quillrun offers an immediate pick-up and delivery of your time sensitive documents and goods, 24 hours a day, 7 days a week.</p>
    </div>
    <div class="offer-item">
      <svg width="60" height="60" viewBox="0 0 60 60"><circle cx="30" cy="30" r="26" fill="#1c5ea8"/><path d="M33 10L18 34h11l-3 16 16-25H31z" fill="#f07f1b"/></svg>
      <h4>Rush</h4>
      <p>Pick up and delivery made within 90 minutes of your call, locally. Add 1 hour for every 50 miles out of town. Available 24 hours a day, 7 days a week.</p>
    </div>
    <div class="offer-item">
      <svg width="60" height="60" viewBox="0 0 60 60"><path d="M30 6l22 11v26L30 54 8 43V17z" fill="#f07f1b"/><path d="M8 17l22 11 22-11M30 28v26" fill="none" stroke="#fff" stroke-width="2.5"/><circle cx="46" cy="12" r="9" fill="#1c5ea8"/><path d="M46 7v5h4" fill="none" stroke="#fff" stroke-width="2"/></svg>
      <h4>Regular Service</h4>
      <p>Pick up and delivery made within 3 hours of your call, locally. Add 1 hour for every 50 miles out of town. Available Monday through Friday.</p>
    </div>
    <div class="offer-item">
      <svg width="60" height="60" viewBox="0 0 60 60"><rect x="6" y="18" width="32" height="26" rx="3" fill="#1c5ea8"/><path d="M38 26h9l7 9v9H38z" fill="#1c5ea8"/><circle cx="16" cy="46" r="5" fill="#f07f1b"/><circle cx="46" cy="46" r="5" fill="#f07f1b"/><path d="M28 6a9 9 0 1 0 9 11 7 7 0 0 1-9-11z" fill="#f07f1b"/></svg>
      <h4>After Hours Delivery</h4>
      <p>Available between 6pm and 8am.</p>
    </div>
  </div>
</section>

<section class="why">
  <div class="why-photo" role="img" aria-label="Photo of a courier's hands holding a brown parcel"></div>
  <svg class="why-panel" width="1200" height="640" viewBox="0 0 1200 640">
    <defs><linearGradient id="whyOrange" x1="0" x2="1"><stop offset="0" stop-color="#f07f1b" stop-opacity=".92"/><stop offset="1" stop-color="#e8953f"/></linearGradient></defs>
    <polygon points="640,0 1200,0 1200,640 560,640" fill="url(#whyOrange)"/>
  </svg>
  <div class="why-content">
    <h2>Why Choose Us</h2>
    <ul class="why-list">
      <li><svg width="18" height="18" viewBox="0 0 18 18"><circle cx="9" cy="9" r="9" fill="#fff"/><path d="M5 9.5l2.6 2.5L13 6.5" fill="none" stroke="#f07f1b" stroke-width="2"/></svg>Money back guaranteed if your package is not delivered on time</li>
      <li><svg width="18" height="18" viewBox="0 0 18 18"><circle cx="9" cy="9" r="9" fill="#fff"/><path d="M5 9.5l2.6 2.5L13 6.5" fill="none" stroke="#f07f1b" stroke-width="2"/></svg>Free waiting time</li>
      <li><svg width="18" height="18" viewBox="0 0 18 18"><circle cx="9" cy="9" r="9" fill="#fff"/><path d="M5 9.5l2.6 2.5L13 6.5" fill="none" stroke="#f07f1b" stroke-width="2"/></svg>All our services are guaranteed</li>
      <li><svg width="18" height="18" viewBox="0 0 18 18"><circle cx="9" cy="9" r="9" fill="#fff"/><path d="M5 9.5l2.6 2.5L13 6.5" fill="none" stroke="#f07f1b" stroke-width="2"/></svg>Pickup within 15 to 30 minutes of your call or sooner</li>
      <li><svg width="18" height="18" viewBox="0 0 18 18"><circle cx="9" cy="9" r="9" fill="#fff"/><path d="M5 9.5l2.6 2.5L13 6.5" fill="none" stroke="#f07f1b" stroke-width="2"/></svg>Fuel charges are free</li>
      <li><svg width="18" height="18" viewBox="0 0 18 18"><circle cx="9" cy="9" r="9" fill="#fff"/><path d="M5 9.5l2.6 2.5L13 6.5" fill="none" stroke="#f07f1b" stroke-width="2"/></svg>State of the art courier software system</li>
      <li><svg width="18" height="18" viewBox="0 0 18 18"><circle cx="9" cy="9" r="9" fill="#fff"/><path d="M5 9.5l2.6 2.5L13 6.5" fill="none" stroke="#f07f1b" stroke-width="2"/></svg>Online ordering</li>
      <li><svg width="18" height="18" viewBox="0 0 18 18"><circle cx="9" cy="9" r="9" fill="#fff"/><path d="M5 9.5l2.6 2.5L13 6.5" fill="none" stroke="#f07f1b" stroke-width="2"/></svg>Online order tracking</li>
      <li><svg width="18" height="18" viewBox="0 0 18 18"><circle cx="9" cy="9" r="9" fill="#fff"/><path d="M5 9.5l2.6 2.5L13 6.5" fill="none" stroke="#f07f1b" stroke-width="2"/></svg>Signature capturing</li>
      <li><svg width="18" height="18" viewBox="0 0 18 18"><circle cx="9" cy="9" r="9" fill="#fff"/><path d="M5 9.5l2.6 2.5L13 6.5" fill="none" stroke="#f07f1b" stroke-width="2"/></svg>Be able to see invoices online</li>
      <li><svg width="18" height="18" viewBox="0 0 18 18"><circle cx="9" cy="9" r="9" fill="#fff"/><path d="M5 9.5l2.6 2.5L13 6.5" fill="none" stroke="#f07f1b" stroke-width="2"/></svg>Be able to print shipping details</li>
    </ul>
  </div>
</section>

<section class="contact">
  <h2 class="section-title">Contact Us</h2>
  <div class="title-rule"></div>
  <div class="contact-form">
    <div class="field">Name</div><div class="field">Email</div>
    <div class="field">Phone</div><div class="field">Street Address</div>
    <div class="field">City or Town</div><div class="field">State</div>
    <div class="field">Zip Code</div><div></div>
    <div class="field wide">Regarding</div>
  </div>
  <span class="btn submit">SUBMIT</span>
</section>

<footer class="site-footer">
  <div class="footer-brand"><span class="brand-square"></span><span class="brand-name">Quillrun Couriers</span></div>
  <div class="footer-col" style="left:504px">
    <h4>Quick Links</h4>
    <ul><li>Home</li><li>About Us</li><li>Services</li><li>Rates</li><li>Customer Benefits</li><li>Contact us</li></ul>
  </div>
  <div class="footer-col" style="left:736px">
    <h4>Contact Info</h4>
    <div class="contact-line"><svg width="14" height="16" viewBox="0 0 14 18"><path d="M7 0a7 7 0 0 0-7 7c0 5 7 11 7 11s7-6 7-11a7 7 0 0 0-7-7z" fill="#f07f1b"/><circle cx="7" cy="7" r="2.5" fill="#1a1a1a"/></svg><span>4820 Harbor Ln,<br>Millbrook, NY 10990 Mailing</span></div>
    <div class="contact-line"><svg width="14" height="16" viewBox="0 0 14 18"><path d="M7 0a7 7 0 0 0-7 7c0 5 7 11 7 11s7-6 7-11a7 7 0 0 0-7-7z" fill="#f07f1b"/><circle cx="7" cy="7" r="2.5" fill="#1a1a1a"/></svg><span>P.O. Box 1187,<br>Lakeview, NY 10993</span></div>
    <div class="contact-line"><svg width="14" height="14" viewBox="0 0 24 24"><path fill="#f07f1b" d="M6.6 10.8a15 15 0 0 0 6.6 6.6l2.2-2.2c.3-.3.7-.4 1-.2 1.1.4 2.3.6 3.6.6.6 0 1 .4 1 1V20c0 .6-.4 1-1 1A17 17 0 0 1 3 4c0-.6.4-1 1-1h3.5c.6 0 1 .4 1 1 0 1.3.2 2.5.6 3.6.1.3 0 .7-.2 1z"/></svg><span>555-014-7170 &nbsp;|&nbsp; 555-018-2427</span></div>
    <div class="contact-line"><svg width="14" height="14" viewBox="0 0 24 24"><path fill="#f07f1b" d="M6.6 10.8a15 15 0 0 0 6.6 6.6l2.2-2.2c.3-.3.7-.4 1-.2 1.1.4 2.3.6 3.6.6.6 0 1 .4 1 1V20c0 .6-.4 1-1 1A17 17 0 0 1 3 4c0-.6.4-1 1-1h3.5c.6 0 1 .4 1 1 0 1.3.2 2.5.6 3.6.1.3 0 .7-.2 1z"/></svg><span>555-016-7041</span></div>
    <div class="contact-line"><svg width="16" height="12" viewBox="0 0 16 12"><rect x="1" y="1" width="14" height="10" fill="none" stroke="#f07f1b" stroke-width="1.6"/><path d="M1 1l7 6 7-6" fill="none" stroke="#f07f1b" stroke-width="1.6"/></svg><span>info@qlnrun.com</span></div>
  </div>
  <div class="footer-bottom">
    <span>© 2021 Quillrun Couriers</span>
    <div class="social"><i></i><i></i><i></i></div>
  </div>
</footer>

</body>
</html>
```